Beacon Advisory Website

I currently have a website www.beaconadvisoryinc.example. We are a IT Consulting Company. Our website will pretty much tell out our services. I am looking to enhance my website and make it look more professional. Looking for very classy and Contemporary look and design for my website.

Industry/Entity Type

It Company

```html
<!DOCTYPE html>
<html lang="en">
<head>
<meta charset="utf-8">
<title>Beacon Advisory</title>
<link href="https://fonts.googleapis.com/css2?family=Open+Sans:wght@400;600;700;800&family=Roboto:wght@400;500&family=Roboto+Condensed:wght@400&display=swap" rel="stylesheet">
<style>
:root{
  --brand:#1a5fa8;
  --sky:#0a9ad8;
  --band:#195ea4;
  --ink:#333;
  --muted:#555;
  --panel:#eeeff1;
  --rule:#cfd3d8;
  --white:#fff;
}
*{margin:0;padding:0;box-sizing:border-box}
html,body{width:949px;height:1200px;overflow:hidden;background:var(--white)}
body{position:relative;font-family:"Roboto",sans-serif;color:var(--ink)}
.abs{position:absolute}

/* header */
.site-header{position:absolute;left:0;top:0;width:949px;height:66px;background:var(--white)}
.brand{position:absolute;left:128px;top:18px;display:flex;align-items:center;gap:7px}
.brand-mark{width:22px;height:22px;background:var(--brand)}
.brand-name{font-family:"Open Sans",sans-serif;font-weight:700;font-size:15px;color:var(--brand)}
.main-nav{position:absolute;left:319px;top:25px;display:flex;align-items:center;font-family:"Open Sans",sans-serif;font-weight:600;font-size:8px;color:#333}
.main-nav a{display:block;padding:0 12px;line-height:21px;text-decoration:none;color:inherit}
.main-nav a.active{background:var(--sky);color:var(--white);padding:0 7px;margin-right:8px}
.phone-box{position:absolute;left:723px;top:20px;width:98px;height:27px;border:2px solid var(--sky);display:flex;align-items:center;font-family:"Roboto Condensed",sans-serif;font-size:12px;color:var(--sky)}
.phone-box .ico{width:22px;height:100%;display:flex;align-items:center;justify-content:center;border-right:1px solid var(--sky);margin-right:5px}

/* hero */
.hero{position:absolute;left:0;top:66px;width:949px;height:344px;background:linear-gradient(90deg,#8c8d8f 0%,#a5a6a8 40%,#6d7178 70%,#b0b2b5 100%)}
.hero-title{position:absolute;left:126px;top:118px;font-family:"Open Sans",sans-serif;font-weight:800;font-size:29px;line-height:35px;color:var(--white);letter-spacing:.5px}
.btn{display:inline-block;background:var(--sky);color:var(--white);font-family:"Open Sans",sans-serif;font-weight:700;letter-spacing:1.3px;text-align:center;border-radius:3px}
.hero .btn{position:absolute;left:129px;top:197px;width:109px;height:29px;line-height:29px;font-size:9px}
.slide-arrow{position:absolute;top:145px;width:52px;height:52px;border-radius:50%;background:var(--sky);display:flex;align-items:center}
.slide-arrow.prev{left:-27px;justify-content:flex-end;padding-right:10px}
.slide-arrow.next{left:922px;justify-content:flex-start;padding-left:10px}

/* welcome */
.welcome-title{position:absolute;left:128px;top:436px;display:flex;align-items:center;gap:9px;font-family:"Open Sans",sans-serif;font-weight:700;font-size:15px;color:var(--sky)}
.welcome-title .mark{width:20px;height:20px;background:var(--brand)}
.welcome-text{position:absolute;left:130px;top:472px;width:307px;font-size:9.4px;line-height:14.9px;color:var(--muted);text-align:justify}
.welcome .btn{position:absolute;left:130px;top:591px;width:87px;height:22px;line-height:22px;font-size:8px}
.video{position:absolute;left:478px;top:430px;width:343px;height:198px;background:linear-gradient(135deg,#c9ccd0,#8f959c 60%,#4b4f55)}
.play{position:absolute;left:145px;top:73px}

/* services */
.services{position:absolute;left:0;top:656px;width:949px;height:330px;background:var(--panel)}
.services h2{position:absolute;left:0;width:949px;top:24px;text-align:center;font-family:"Open Sans",sans-serif;font-weight:700;font-size:16px;color:var(--sky)}
.services .underline{position:absolute;left:420px;top:47px;width:108px;height:2px;background:var(--sky)}
.svc{position:absolute;text-align:center}
.svc svg{display:block;margin:0 auto}
.svc h3{font-family:"Open Sans",sans-serif;font-weight:600;font-size:11px;color:var(--brand);margin-top:10px;letter-spacing:.2px}
.svc p{font-size:9.4px;line-height:14.5px;color:var(--muted);margin-top:6px}
.vrule{position:absolute;width:1px;background:var(--rule)}
.hrule{position:absolute;height:1px;background:var(--rule)}

/* band */
.band{position:absolute;left:0;top:986px;width:949px;height:73px;background:var(--band)}
.band-item{position:absolute;top:17px;display:flex;gap:18px}
.band-item h4{font-family:"Open Sans",sans-serif;font-weight:600;font-size:12px;color:var(--white);letter-spacing:.3px}
.band-item .tag{display:inline-block;margin-top:5px;background:var(--sky);color:var(--white);font-family:"Open Sans",sans-serif;font-size:7.5px;padding:4px 7px}
.band-sep{position:absolute;top:0;width:1px;height:73px;background:#2c6fb3}

/* footer */
.site-footer{position:absolute;left:0;top:1059px;width:949px;height:141px;background:var(--sky);color:var(--white)}
.site-footer h5{position:absolute;top:26px;font-family:"Open Sans",sans-serif;font-weight:700;font-size:9px;letter-spacing:.2px}
.address{position:absolute;left:127px;top:55px;font-size:8px;line-height:14.5px}
.address strong{font-family:"Open Sans",sans-serif;font-weight:600}
.email{position:absolute;left:307px;top:54px;width:163px;height:28px;background:var(--white);display:flex;align-items:center;padding-left:12px;gap:7px;font-size:8px;color:#666}
.signup{position:absolute;left:398px;top:89px;width:72px;height:25px;line-height:25px;text-align:center;background:var(--band);font-family:"Open Sans",sans-serif;font-weight:700;font-size:9px}
.social{position:absolute;left:530px;top:50px;display:flex;gap:8px}
.social span{width:22px;height:22px;border-radius:50%;background:var(--band)}
.social span.feed{background:#e85a2b}
.footer-brand{position:absolute;left:700px;top:48px;display:flex;align-items:center;gap:7px}
.footer-brand .mark{width:22px;height:22px;background:var(--white)}
.footer-brand .name{font-family:"Open Sans",sans-serif;font-weight:700;font-size:15px}
.copyright{position:absolute;left:688px;top:108px;font-size:7.5px}
</style>
</head>
<body>

<header class="site-header">
  <div class="brand"><span class="brand-mark"></span><span class="brand-name">Beacon Advisory</span></div>
  <nav class="main-nav">
    <a class="active" href="#">COMPANY</a>
    <a href="#">SERVICES</a>
    <a href="#">SOLUTIONS</a>
    <a href="#">RESOURCES</a>
    <a href="#">CAREER</a>
    <a href="#">CONTACT US</a>
  </nav>
  <div class="phone-box">
    <span class="ico"><svg width="10" height="10" viewBox="0 0 24 24"><path fill="#0a9ad8" d="M6.6 10.8a15 15 0 006.6 6.6l2.2-2.2c.3-.3.7-.4 1-.2 1.1.4 2.3.6 3.6.6.6 0 1 .4 1 1V20c0 .6-.4 1-1 1A17 17 0 013 4c0-.6.4-1 1-1h3.5c.6 0 1 .4 1 1 0 1.3.2 2.5.6 3.6.1.3 0 .7-.2 1z"/></svg></span>
    (555) 014 2290
  </div>
</header>

<section class="hero">
  <div class="abs" role="img" aria-label="Businessman touching a glowing network of connected people icons" style="left:0;top:0;width:949px;height:344px"></div>
  <h1 class="hero-title">BUSINESS<br>CONSULTING</h1>
  <a class="btn">READ MORE</a>
  <div class="slide-arrow prev"><svg width="10" height="12" viewBox="0 0 10 12"><path d="M7 1L2 6l5 5" stroke="#fff" stroke-width="2.4" fill="none"/></svg></div>
  <div class="slide-arrow next"><svg width="10" height="12" viewBox="0 0 10 12"><path d="M3 1l5 5-5 5" stroke="#fff" stroke-width="2.4" fill="none"/></svg></div>
</section>

<section class="welcome">
  <h2 class="welcome-title"><span class="mark"></span>WELCOME TO OUR SITE</h2>
  <p class="welcome-text">Today's IT market is a dynamic, fast-paced industry, with ever-increasing demands. Meeting these demands for over 25 years, Beacon Advisory maintains a global presence, aggressively recruiting expertly qualified IT and Management Professionals from around the world and cultivating key partnerships with corporations to understand their business models end-to-end, with a goal of delivering exceptional client service and ensuring a consistent delivery of the talent needed to drive results.</p>
  <a class="btn">READ MORE</a>
  <div class="video" role="img" aria-label="Video still of a smiling businessman in a suit in a bright office">
    <svg class="play" width="54" height="54" viewBox="0 0 54 54"><circle cx="27" cy="27" r="25" fill="none" stroke="#fff" stroke-width="3"/><path d="M21 16l18 11-18 11z" fill="#fff"/></svg>
  </div>
</section>

<section class="services">
  <h2>OUR SERVICES</h2>
  <div class="underline"></div>

  <div class="svc" style="left:126px;top:70px;width:200px">
    <svg width="34" height="34" viewBox="0 0 34 34" fill="none" stroke="#1a5fa8" stroke-width="1.8"><rect x="7" y="7" width="20" height="20"/><rect x="13" y="13" width="8" height="8"/><path d="M11 2v5M17 2v5M23 2v5M11 27v5M17 27v5M23 27v5M2 11h5M2 17h5M2 23h5M27 11h5M27 17h5M27 23h5"/></svg>
    <h3>TECHNOLOGY</h3>
    <p>Beacon Advisory Training programs are perfect for individuals to enhance their careers.</p>
  </div>
  <div class="vrule" style="left:350px;top:67px;height:96px"></div>
  <div class="svc" style="left:374px;top:70px;width:200px">
    <svg width="34" height="34" viewBox="0 0 34 34" fill="#1a5fa8"><rect x="3" y="20" width="5" height="11"/><rect x="10" y="15" width="5" height="16"/><rect x="17" y="10" width="5" height="21"/><rect x="24" y="4" width="5" height="27"/></svg>
    <h3>BUSINESS</h3>
    <p>Our Offshore development model has a unique distinction of providing efficient software ...</p>
  </div>
  <div class="vrule" style="left:598px;top:67px;height:96px"></div>
  <div class="svc" style="left:620px;top:70px;width:202px">
    <svg width="34" height="34" viewBox="0 0 34 34"><path d="M4 4h26v20H14l-7 6v-6H4z" fill="none" stroke="#1a5fa8" stroke-width="2.4"/><circle cx="11" cy="14" r="2" fill="#1a5fa8"/><circle cx="17" cy="14" r="2" fill="#1a5fa8"/><circle cx="23" cy="14" r="2" fill="#1a5fa8"/></svg>
    <h3>IT CONSULTING</h3>
    <p>Beacon Advisory Training programs are perfect for individuals to enhance their careers.</p>
  </div>

  <div class="hrule" style="left:126px;top:185px;width:203px"></div>
  <div class="hrule" style="left:377px;top:185px;width:202px"></div>
  <div class="hrule" style="left:623px;top:185px;width:202px"></div>

  <div class="svc" style="left:146px;top:207px;width:290px">
    <svg width="34" height="34" viewBox="0 0 34 34" fill="#1a5fa8"><rect x="2" y="12" width="10" height="9"/><rect x="14" y="12" width="10" height="9"/><rect x="2" y="23" width="10" height="9"/><rect x="14" y="23" width="10" height="9"/><circle cx="26" cy="8" r="6"/><circle cx="26" cy="8" r="2.2" fill="#eeeff1"/></svg>
    <h3>APPLICATION DEVELOPMENT</h3>
    <p>Drawing on our experience in all major industries, we develop solutions that meet the most challenging IT problems.</p>
  </div>
  <div class="vrule" style="left:447px;top:213px;height:92px"></div>
  <div class="svc" style="left:462px;top:207px;width:312px">
    <svg width="34" height="34" viewBox="0 0 34 34" fill="#1a5fa8"><rect x="9" y="9" width="16" height="16" transform="rotate(45 17 17)"/><circle cx="17" cy="4" r="3.5"/><circle cx="17" cy="30" r="3.5"/><circle cx="4" cy="17" r="3.5"/><circle cx="30" cy="17" r="3.5"/></svg>
    <h3>ENTERPRISE INTEGRATION</h3>
    <p>As organizations work to achieve and sustain competitive advantage, the ability for IT departments to demonstrate their value..</p>
  </div>
</section>

<section class="band">
  <div class="band-item" style="left:160px">
    <svg width="34" height="28" viewBox="0 0 34 28" fill="#fff"><circle cx="7" cy="5" r="3"/><circle cx="27" cy="5" r="3"/><rect x="4" y="9" width="6" height="9"/><rect x="24" y="9" width="6" height="9"/><rect x="10" y="14" width="14" height="2"/><rect x="2" y="20" width="30" height="2"/><rect x="5" y="22" width="2" height="5"/><rect x="27" y="22" width="2" height="5"/></svg>
    <div><h4>CONSULTING</h4><span class="tag">READ MORE</span></div>
  </div>
  <div class="band-sep" style="left:352px"></div>
  <div class="band-item" style="left:396px">
    <svg width="38" height="28" viewBox="0 0 38 28" fill="#fff"><circle cx="19" cy="7" r="5"/><circle cx="8" cy="10" r="4"/><circle cx="30" cy="10" r="4"/><path d="M11 26c0-7 4-11 8-11s8 4 8 11z"/><path d="M1 26c0-6 3-9 7-9 2 0 3 1 4 2-1 2-2 4-2 7zM37 26c0-6-3-9-7-9-2 0-3 1-4 2 1 2 2 4 2 7z"/></svg>
    <div><h4>STAFF AUGMENTATION</h4><span class="tag">READ MORE</span></div>
  </div>
  <div class="band-sep" style="left:638px"></div>
  <div class="band-item" style="left:683px">
    <svg width="24" height="24" viewBox="0 0 24 24"><circle cx="12" cy="12" r="11" fill="#fff"/><path d="M6 7c2-1 4 0 5 2s-1 3-3 3-2 3-4 2M14 4c2 1 3 3 2 4s-3 0-3 2 3 2 5 4-1 5-3 6" fill="#195ea4"/></svg>
    <div><h4>OFFSHORE</h4><span class="tag">READ MORE</span></div>
  </div>
</section>

<footer class="site-footer">
  <h5 style="left:127px">CONTACT US</h5>
  <p class="address"><strong>HEAD OFFICE</strong><br>480 Harbor Lane, Suite 12<br>Westbrook, NJ 00000<br>Phone: +1 (555) 014 2290</p>

  <h5 style="left:307px">NEWSLETTER SIGNUP!</h5>
  <div class="email"><svg width="9" height="7" viewBox="0 0 9 7"><rect width="9" height="7" fill="#555"/><path d="M0 0l4.5 4L9 0" stroke="#fff" fill="none"/></svg>E mail id</div>
  <div class="signup">SIGNUP!</div>

  <h5 style="left:532px">FOLLOW US ON</h5>
  <div class="social" aria-label="Social links"><span></span><span></span><span></span><span class="feed"></span></div>

  <div class="footer-brand"><span class="mark"></span><span class="name">Beacon Advisory</span></div>
  <p class="copyright">Copyrights @ 2016 All Rights Reserved</p>
</footer>

</body>
</html>
```